Web Design Project

Looking for a web page design for a consulting company called Tessaro Consulting.

Tessaro specialize in Business Improvement and Transformation consulting in the Mining, Infrastructure, Logistics and Transport sectors.
Updates

Industry/Entity Type

Business

Font styles to use
Sans Serif

Colors
86cae7
0892cd
ecf7f5

```html
<!DOCTYPE html>
<html lang="en">
<head>
<meta charset="utf-8">
<title>Tessaro Consulting</title>
<link rel="stylesheet" href="https://fonts.googleapis.com/css2?family=Cinzel:wght@400;500&family=Open+Sans:wght@400;600;700&display=swap">
<style>
  :root {
    --sky: #86cae7;
    --brand: #0892cd;
    --tab: #2a9fd6;
    --mint: #ecf7f5;
    --ink: #333333;
    --ink-soft: #444444;
    --rule: #cfcfcf;
    --card-line: #c9c9c9;
    --white: #ffffff;
  }
  * { box-sizing: border-box; margin: 0; padding: 0; }
  html, body { width: 903px; height: 1200px; overflow: hidden; background: var(--white); }
  body { font-family: "Open Sans", Arial, sans-serif; color: var(--ink); position: relative; }

  .site-header { position: absolute; left: 0; top: 0; width: 903px; height: 117px; }
  .brand { position: absolute; left: 20px; top: 54px; display: flex; align-items: center; gap: 8px;
    font-family: "Cinzel", Georgia, serif; font-size: 17px; color: var(--brand); letter-spacing: 1px; }
  .brand-dot { width: 14px; height: 14px; border-radius: 50%; background: var(--brand); }
  .main-nav { position: absolute; left: 272px; top: 0; display: flex; height: 117px; }
  .main-nav a { display: flex; align-items: flex-end; padding: 0 21px 8px; height: 117px;
    font-family: "Cinzel", Georgia, serif; font-size: 12.5px; color: var(--ink-soft); text-decoration: none; letter-spacing: .3px; }
  .main-nav a.is-active { background: var(--tab); color: var(--white); padding: 0 20px 8px; }

  .hero { position: absolute; left: 11px; top: 131px; width: 885px; height: 391px;
    background: linear-gradient(100deg, #d7dde2 0%, #eef3f6 35%, #c8cfd6 60%, #dfe6ea 100%); }

  .sectors { position: absolute; left: 15px; top: 547px; display: flex; gap: 10px; }
  .sector-card { width: 212px; height: 277px; border: 1px solid var(--card-line); padding: 2px; text-align: center; }
  .sector-photo { height: 148px; }
  .photo-mining { background: linear-gradient(180deg, #7aa6d6 0%, #c7d8e8 45%, #d89a4a 75%, #b5692a 100%); }
  .photo-infra { background: linear-gradient(180deg, #4c6d9a 0%, #9aa6b3 45%, #c08a55 70%, #4a4a52 100%); }
  .photo-logistics { background: linear-gradient(180deg, #8ea7c0 0%, #e3c7a4 45%, #5a78a8 75%, #6d6d6d 100%); }
  .photo-transport { background: linear-gradient(180deg, #8fb3d8 0%, #c9d9e6 40%, #d9a23a 65%, #7a6e60 100%); }
  .sector-title { font-family: "Cinzel", Georgia, serif; font-size: 19px; font-weight: 400; color: var(--ink); margin-top: 7px; letter-spacing: .5px; }
  .sector-text { font-size: 11px; line-height: 11.5px; color: var(--ink-soft); margin: 8px 12px 0; }
  .btn-more { display: inline-block; margin-top: 15px; width: 84px; height: 28px; line-height: 28px; border-radius: 3px;
    background: var(--sky); color: var(--white); font-size: 12px; font-weight: 700; font-style: italic; text-decoration: none; }

  .section-title { font-family: "Cinzel", Georgia, serif; font-size: 25px; font-weight: 400; color: var(--ink); letter-spacing: .5px; }
  .testimonials { position: absolute; left: 18px; top: 869px; width: 320px; }
  .quote { position: relative; padding-left: 33px; margin-top: 20px; font-size: 13.8px; line-height: 15.7px; color: var(--ink-soft); }
  .quote + .quote { margin-top: 49px; }
  .quote svg { position: absolute; left: 3px; top: 4px; }
  .quote-author { display: block; color: var(--brand); font-weight: 600; font-style: normal; }

  .about { position: absolute; left: 374px; top: 869px; width: 512px; }
  .about-body { margin-top: 20px; font-size: 13.8px; line-height: 15.7px; color: var(--ink-soft); }
  .about-photo { float: left; width: 258px; height: 174px; margin: 0 13px 6px 2px;
    background: linear-gradient(110deg, #d9dee3 0%, #f1f3f4 40%, #c9b7a8 70%, #6c7480 100%); }

  .site-footer { position: absolute; left: 14px; top: 1152px; width: 878px; border-top: 1px solid var(--rule);
    display: flex; justify-content: space-between; padding: 17px 4px 0 4px; font-size: 12px; color: var(--ink-soft); }
  .footer-nav a { color: var(--ink-soft); text-decoration: none; }
  .footer-nav span { margin: 0 4px; }
</style>
</head>
<body>
  <header class="site-header">
    <div class="brand"><span class="brand-dot"></span>Tessaro Consulting</div>
    <nav class="main-nav">
      <a class="is-active" href="#">Home</a>
      <a href="#">About Us</a>
      <a href="#">Services</a>
      <a href="#">Testimonials</a>
      <a href="#">News</a>
      <a href="#">Contact Us</a>
    </nav>
  </header>

  <div class="hero" role="img" aria-label="Team of four business consultants gathered around a laptop in a bright office"></div>

  <section class="sectors">
    <article class="sector-card">
      <div class="sector-photo photo-mining" role="img" aria-label="Excavator loading a dump truck at a mine site"></div>
      <h3 class="sector-title">Mining</h3>
      <p class="sector-text">Lorem ipsum dolor sit amet, consectetuer adipiscing elit, sed diam nonummy nibh euismod</p>
      <a class="btn-more" href="#">MORE</a>
    </article>
    <article class="sector-card">
      <div class="sector-photo photo-infra" role="img" aria-label="Elevated highway interchange at dusk with light trails"></div>
      <h3 class="sector-title">Infrastructure</h3>
      <p class="sector-text">Lorem ipsum dolor sit amet, consectetuer adipiscing elit, sed diam nonummy nibh euismod</p>
      <a class="btn-more" href="#">MORE</a>
    </article>
    <article class="sector-card">
      <div class="sector-photo photo-logistics" role="img" aria-label="Blue freight truck with trailers on a road at sunset"></div>
      <h3 class="sector-title">Logistics</h3>
      <p class="sector-text">Lorem ipsum dolor sit amet, consectetuer adipiscing elit, sed diam nonummy nibh euismod</p>
      <a class="btn-more" href="#">MORE</a>
    </article>
    <article class="sector-card">
      <div class="sector-photo photo-transport" role="img" aria-label="Yellow and red passenger train on railway tracks"></div>
      <h3 class="sector-title">Transportation</h3>
      <p class="sector-text">Lorem ipsum dolor sit amet, consectetuer adipiscing elit, sed diam nonummy nibh euismod</p>
      <a class="btn-more" href="#">MORE</a>
    </article>
  </section>

  <section class="testimonials">
    <h2 class="section-title">Testimonials</h2>
    <blockquote class="quote">
      <svg width="20" height="12" viewBox="0 0 20 12" aria-hidden="true"><path d="M3 0h5L5 12H0zM13 0h5l-3 12h-5z" fill="var(--sky)"/></svg>
      Lorem ipsum dolor sit amet, consec tetuer adipiscing. Praesent vestibu lum molestie lacuiirhs. Aenean non ummy hendreriauris. Phasellllus.
      <cite class="quote-author">Carys L.</cite>
    </blockquote>
    <blockquote class="quote">
      <svg width="20" height="12" viewBox="0 0 20 12" aria-hidden="true"><path d="M3 0h5L5 12H0zM13 0h5l-3 12h-5z" fill="var(--sky)"/></svg>
      Duis autem vel eum iriure dolor in hendrerit in vulputate velit esse molestie consequat, vel illum dolore eu feugiat nulla facilisis at vero eros et accumsan.
      <cite class="quote-author">Rowan T.</cite>
    </blockquote>
  </section>

  <section class="about">
    <h2 class="section-title">About Tessaro Consulting</h2>
    <div class="about-body">
      <div class="about-photo" role="img" aria-label="Three colleagues reviewing a printed chart together"></div>
      Typi non habent claritatem insitam; est usus legentis in iis qui facit eorum claritatem. Investigationes demonstraverunt lectores legere me lius quod ii legunt saepius. Claritas est etiam processus dynamicus, qui sequitur mutationem consuetudium lectorum. Mirum est notare quam littera gothica, quam nunc putamus parum claram, anteposuerit litterarum formas humanitatis per seacula quarta decima et quinta decima. Eodem modo typi, qui nunc nobis videntur parum clari, fiant sollemnes in futurum.
    </div>
  </section>

  <footer class="site-footer">
    <span>2013 © Privacy Policy</span>
    <nav class="footer-nav">
      <a href="#">Home</a><span>·</span><a href="#">About Us</a><span>·</span><a href="#">Services</a><span>·</span><a href="#">Testimonials</a><span>·</span><a href="#">News</a><span>·</span><a href="#">Contact Us</a>
    </nav>
  </footer>
</body>
</html>
```